Comprehensive guide for the front desk medical office staff.

selling a reference guide for the front desk personnel at Urgent Care clinics

Target Market(s)

Urgent Care and physian office manager s

Industry/Entity Type

Medical

```html
<!DOCTYPE html>
<html lang="en">
<head>
<meta charset="utf-8">
<title>Front Desk Reference Guide Poster</title>
<link rel="stylesheet" href="https://fonts.googleapis.com/css2?family=Roboto+Condensed:ital,wght@0,400;0,700;1,700&display=swap">
<style>
  :root {
    --navy: #0a3350;
    --yellow: #ffd21f;
    --sky: #3cb4e7;
    --red: #e5432d;
    --white: #ffffff;
    --stage: #e8e9ea;
    --panel-light: #efefef;
    --panel-shade: #e2e2e2;
  }
  * { margin: 0; padding: 0; box-sizing: border-box; }
  html, body { width: 1200px; height: 1200px; overflow: hidden; }
  body {
    background: var(--stage);
    font-family: "Roboto Condensed", "Arial Narrow", sans-serif;
    position: relative;
  }
  .poster {
    position: absolute;
    left: 210px; top: 23px;
    width: 780px; height: 1154px;
    background: var(--navy);
    overflow: hidden;
  }
  .poster > * { position: absolute; }
  .waves { left: 0; top: 0; width: 780px; height: 1154px; }

  .author-line {
    top: 45px; left: 0; width: 100%;
    display: flex; justify-content: center; align-items: center; gap: 18px;
  }
  .author-line .rule { width: 178px; height: 14px; }
  .author-name { color: var(--white); font-weight: 700; font-size: 31px; letter-spacing: -0.3px; }

  .kicker {
    top: 98px; width: 100%; text-align: center;
    color: var(--yellow); font-weight: 700; font-size: 36px; letter-spacing: -0.2px;
  }
  .title {
    top: 145px; width: 100%; text-align: center;
    color: var(--sky); font-weight: 700; font-size: 66px; line-height: 60px; letter-spacing: -0.5px;
    white-space: nowrap;
  }
  .subtitle {
    top: 272px; width: 100%; text-align: center;
    color: var(--sky); font-weight: 700; font-size: 28px; line-height: 40px;
  }

  .info-card {
    left: 164px; top: 491px; width: 178px; height: 243px;
    background: var(--navy);
    box-shadow: 2px 4px 5px rgba(0,0,0,0.35);
    text-align: center; color: var(--white);
    padding-top: 22px;
  }
  .info-card .card-label { color: var(--yellow); font-weight: 700; font-size: 20px; line-height: 24px; }
  .info-card .card-author { font-weight: 700; font-style: italic; font-size: 22px; margin-top: 16px; }
  .info-card .card-text { font-size: 16.5px; line-height: 21px; margin-top: 6px; }

  .buy-button {
    left: 159px; top: 766px; width: 180px; height: 43px;
    background: var(--red); color: var(--white);
    font-weight: 700; font-style: italic; font-size: 31px;
    display: flex; align-items: center; justify-content: center;
  }

  .features {
    top: 868px; left: 90px; list-style: none;
    color: var(--white); font-weight: 700; font-size: 25px; line-height: 31px;
  }
  .features li { display: flex; align-items: center; gap: 8px; }
  .features svg { width: 26px; height: 24px; flex: none; }

  .order-line {
    top: 1006px; width: 100%; text-align: center;
    color: var(--white); font-weight: 700; font-size: 58px; letter-spacing: -0.5px;
  }
  .price-line {
    top: 1070px; width: 100%; text-align: center;
    color: var(--yellow); font-weight: 700; font-size: 30px;
  }
</style>
</head>
<body>
<main class="poster">
  <svg class="waves" viewBox="0 0 780 1154">
    <defs>
      <linearGradient id="panelFill" x1="0" y1="0" x2="1" y2="0">
        <stop offset="0" stop-color="#efefef"/>
        <stop offset="1" stop-color="#e2e2e2"/>
      </linearGradient>
      <linearGradient id="photoFill" x1="0" y1="0" x2="1" y2="1">
        <stop offset="0" stop-color="#f6f1ee"/>
        <stop offset="0.5" stop-color="#e9c9b4"/>
        <stop offset="1" stop-color="#f4efec"/>
      </linearGradient>
      <clipPath id="panelClip">
        <path d="M0,517 C120,440 240,395 420,372 C560,358 690,380 780,420 L780,748 C600,850 300,880 0,808 Z"/>
      </clipPath>
    </defs>
    <path d="M0,517 C120,440 240,395 420,372 C560,358 690,380 780,420 L780,748 C600,850 300,880 0,808 Z" fill="url(#panelFill)"/>
    <rect x="413" y="340" width="367" height="540" fill="url(#photoFill)" clip-path="url(#panelClip)" role="img" aria-label="Photo of a mother holding her baby close"/>
    <path d="M0,478 C110,420 230,385 380,373 L420,372 C240,395 120,440 0,517 Z" fill="#ffd21f"/>
    <path d="M780,712 C650,800 540,840 420,856 C560,846 680,810 780,748 Z" fill="#ffd21f"/>
  </svg>

  <header class="author-line">
    <svg class="rule" viewBox="0 0 178 14" aria-hidden="true"><g stroke="#ffffff" stroke-width="1.5"><line x1="0" y1="2" x2="178" y2="2"/><line x1="0" y1="7" x2="178" y2="7"/><line x1="0" y1="12" x2="178" y2="12"/></g></svg>
    <span class="author-name">Laura Whitfield</span>
    <svg class="rule" viewBox="0 0 178 14" aria-hidden="true"><g stroke="#ffffff" stroke-width="1.5"><line x1="0" y1="2" x2="178" y2="2"/><line x1="0" y1="7" x2="178" y2="7"/><line x1="0" y1="12" x2="178" y2="12"/></g></svg>
  </header>

  <p class="kicker">FRONT DESK REFERENCE GUIDE FOR</p>
  <h1 class="title">WALK-IN CLINICS AND<br>FAMILY PRACTICES</h1>
  <p class="subtitle">Glossary of medical terminology used by front office<br>medical staff and insurance companies</p>

  <aside class="info-card">
    <p class="card-label">DESK<br>INSURANCE<br>CARD</p>
    <p class="card-author">Laura Whitfield</p>
    <p class="card-text">shares over a decade<br>of medical office<br>experience in this<br>comprehensive guide.</p>
  </aside>
  <div class="buy-button">BUY NOW</div>

  <ul class="features">
    <li><svg viewBox="0 0 26 24"><path d="M2,13 L9,20 L24,3" fill="none" stroke="#ffd21f" stroke-width="4.5" stroke-linecap="round" stroke-linejoin="round"/></svg>Shows staff how to read an insurance card.</li>
    <li><svg viewBox="0 0 26 24"><path d="M2,13 L9,20 L24,3" fill="none" stroke="#ffd21f" stroke-width="4.5" stroke-linecap="round" stroke-linejoin="round"/></svg>What is a deductible and when to collect a copay.</li>
    <li><svg viewBox="0 0 26 24"><path d="M2,13 L9,20 L24,3" fill="none" stroke="#ffd21f" stroke-width="4.5" stroke-linecap="round" stroke-linejoin="round"/></svg>What is Workers comp.</li>
    <li><svg viewBox="0 0 26 24"><path d="M2,13 L9,20 L24,3" fill="none" stroke="#ffd21f" stroke-width="4.5" stroke-linecap="round" stroke-linejoin="round"/></svg>Information in HIPAA guidelines and insurance plans.</li>
  </ul>

  <p class="order-line">To order call 555-214-7390</p>
  <p class="price-line">Price is $99.99 plus $7.00 shipping and handling</p>
</main>
</body>
</html>
```